Website for cloud company, IaaS, KRD competitor

We are looking for a new website, logo, and design elements for our existing website, www.boundlesshost.com. The first phase is to design a product page that can be integrated into an overall site. So at this point, I am looking for a designer to create a design for our product http://www.boundlesshost.com/categories/ledgerpro-hosting/loopapp-ledgerpro.html. We would like this to be a mobile site that scrolls vertically to get customer to see more and more information about our product. Here are some other pages with information we want to reference:
http://www.boundlesshost.com/compare-ledgerpro.html
http://www.boundlesshost.com/ada.html
http://www.boundlesshost.com/our-stories.html
http://www.boundlesshost.com/our-guarantee.html
Updates

Project Deadline Extended
Reason: Due to the holidays, I am extending the deadline by 5 days. Please get me your best designs. Thank you for your effort.

Target Market(s)

We are a hosting company. We target small and medium business.

Industry/Entity Type

It Company

Logo Text

Boundless Host

Number of Pages Required

1 page

Font styles to use
Sans Serif

Requirements
Must have
• 1. the major design color should be similar to our existing website to preserve brand
• 2. logo must be 2d but reference the infinite symbol
• 3. product page must have a grid for pricing
• 4. product page must have a simple nav with products, industries, support, contact us,
• 5. page must have visible phone number and login for existing customers

```html
<!DOCTYPE html>
<html lang="en">
<head>
<meta charset="utf-8">
<title>Boundless Host – Effortless Cloud Computing</title>
<link href="https://fonts.googleapis.com/css2?family=Oswald:wght@300;400;500&family=Roboto:wght@300;400;500;700&display=swap" rel="stylesheet">
<style>
:root{
  --maroon:#4a0d0d;
  --maroon-mid:#7a1a1a;
  --navy:#2b3a55;
  --blue:#4a9ad8;
  --teal:#2fa39c;
  --plum:#955b7a;
  --amber:#f4b24e;
  --ink:#333;
  --muted:#777;
  --line:#ddd;
  --panel:#f2f2f2;
  --accent:#c0392b;
}
*{margin:0;padding:0;box-sizing:border-box}
html,body{width:1200px;height:2791px;overflow:hidden}
body{position:relative;font-family:"Roboto",sans-serif;color:var(--ink);background:#fff}
.abs{position:absolute}

/* header */
.site-header{position:absolute;left:0;top:0;width:1200px;height:86px;background:var(--maroon);z-index:3}
.brand{position:absolute;left:102px;top:24px;display:flex;align-items:center;gap:12px;color:#fff;font-size:24px;font-weight:400;letter-spacing:1px;text-transform:uppercase}
.brand-mark{width:30px;height:30px;border-radius:50%;background:#fff}
.menu{position:absolute;left:346px;top:0;width:114px;background:var(--maroon-mid)}
.menu-toggle{height:86px;line-height:86px;padding-left:14px;color:#fff;font-size:13px;font-weight:700}
.menu-list{list-style:none}
.menu-list li{height:38px;line-height:38px;padding-left:14px;color:#fff;font-size:12px;font-weight:500;border-top:1px solid rgba(255,255,255,.25)}
.phone{position:absolute;left:731px;top:34px;color:#fff;font-size:14px}
.login{position:absolute;left:846px;top:30px;width:66px;height:26px;border-radius:3px;background:#eee;color:var(--ink);font-size:12px;font-weight:500;text-align:center;line-height:26px}
.tools{position:absolute;left:986px;top:31px;display:flex;align-items:center;gap:16px;color:#fff;font-size:14px}

/* hero */
.hero{position:absolute;left:0;top:86px;width:1200px;height:437px;background:linear-gradient(180deg,#b9c4e0 0%,#dcd6ec 45%,#f2e6ee 70%,#e9eaf3 100%)}
.hero-server{position:absolute;left:690px;top:20px;width:300px;height:390px;background:linear-gradient(90deg,#2a2a2a,#111 50%,#3a3a3a);border-radius:4px}
.hero-title{position:absolute;left:97px;top:200px;font-family:"Oswald",sans-serif;color:#1c1c1c}
.hero-title .l1{display:block;font-size:54px;font-weight:500;line-height:68px}
.hero-title .l2{display:block;font-size:50px;font-weight:300;line-height:66px}
.hero-arrow{position:absolute;top:244px;width:40px;height:40px}

/* welcome */
.welcome{position:absolute;left:0;top:523px;width:1200px;height:323px;text-align:center}
.welcome h1{position:absolute;left:0;width:1200px;top:36px;font-size:27px;font-weight:400;color:#444}
.welcome h2{position:absolute;left:0;width:1200px;top:74px;font-size:17px;font-weight:500;color:#222}
.welcome p{position:absolute;left:115px;width:970px;top:114px;font-size:11.5px;line-height:22px;color:var(--muted);text-align:left}
.btn-dark{position:absolute;left:543px;top:240px;width:114px;height:41px;background:#2a2a2a;color:#fff;border-radius:3px;font-size:12px;font-weight:500;line-height:41px;text-align:center}

/* pricing */
.pricing{position:absolute;left:0;top:846px;width:1200px;height:694px;background:var(--maroon);color:#fff;text-align:center}
.pricing h2{position:absolute;left:0;width:1200px;top:32px;font-size:26px;font-weight:400}
.pricing .intro{position:absolute;left:160px;width:880px;top:80px;font-size:12px;line-height:21px}
.plan{position:absolute;top:173px;width:229px;background:#fff;box-shadow:0 10px 14px -6px rgba(0,0,0,.6)}
.plan-name{height:41px;line-height:41px;background:var(--navy);font-size:17px;font-weight:300}
.plan-price{height:145px;display:flex;align-items:center;justify-content:center}
.price-ring{width:104px;height:104px;border:3px solid #fff;border-radius:50%;display:flex;flex-direction:column;align-items:center;justify-content:center}
.price-ring b{font-size:22px;font-weight:500}
.price-ring span{font-size:12px}
.plan-features{list-style:none;padding:0 10px}
.plan-features li{height:49px;line-height:49px;color:#555;font-size:15px;font-weight:300;border-bottom:1px solid var(--line)}
.plan-features li:last-child{border-bottom:0}
.plan-cta{height:37px;line-height:37px;font-size:15px;color:#fff}
.blue{background:var(--blue)}.teal{background:var(--teal)}.plum{background:var(--plum)}.amber{background:var(--amber)}

/* content */
.section-title{position:absolute;left:99px;font-size:26px;font-weight:400;color:#333}
.media{position:absolute;left:99px;width:686px;border:3px solid #e2e2e2}
.body-text{position:absolute;left:99px;width:686px;font-size:11.5px;line-height:20px;color:#555}
.read-more{position:absolute;left:99px;font-size:11px;font-style:italic;color:var(--accent)}
.btn-outline{position:absolute;left:309px;top:2504px;width:253px;height:54px;background:#f4f4f4;border:1px solid #bbb;font-size:17px;line-height:52px;text-align:center;color:#333}

.features{position:absolute;left:818px;top:1583px;width:283px;height:620px;border:1px solid #bbb;background:var(--panel)}
.features h3{height:52px;line-height:52px;background:#2b2b2b;color:#fff;text-align:center;font-size:24px;font-weight:400}
.features ul{list-style:none;padding:20px 0 0 20px}
.features li{height:33.5px;display:flex;align-items:center;gap:10px;font-size:11.5px;color:#333}
.features li svg{flex:none}

.guarantee-seal{position:absolute;left:869px;top:2220px;width:180px;height:180px;border-radius:50%;background:radial-gradient(circle,#d9b876 0%,#b8904a 70%,#8d6a30 100%)}
.partners{position:absolute;left:818px;top:2425px;width:283px;height:133px;border:1px solid #bbb;display:flex;align-items:center;justify-content:space-around;padding:0 10px}
.partner{background:#d8d8d8}

/* footer */
.site-footer{position:absolute;left:0;top:2595px;width:1200px;height:196px;background:var(--maroon);color:#fff}
.foot-col{position:absolute;top:38px;list-style:none;font-size:12px;font-weight:500;line-height:22px}
.foot-rule{position:absolute;top:38px;width:1px;height:94px;background:rgba(255,255,255,.3)}
.social li{display:flex;align-items:center;gap:10px}
.social i{display:inline-block;width:8px;height:8px;background:#fff}
.copyright{position:absolute;left:99px;top:154px;font-size:12px}
.page-code{position:absolute;left:1070px;top:154px;font-size:12px}
</style>
</head>
<body>

<header class="site-header">
  <div class="brand"><span class="brand-mark"></span>Boundless Host</div>
  <nav class="menu">
    <div class="menu-toggle">MENU &#8964;</div>
    <ul class="menu-list">
      <li>PRODUCTS</li><li>INDUSTRIES</li><li>SUPPORT</li><li>CONTACT US</li>
    </ul>
  </nav>
  <div class="phone">1.800.555.0142</div>
  <div class="login">LOGIN</div>
  <div class="tools">
    <svg width="16" height="16" viewBox="0 0 16 16"><circle cx="6.5" cy="6.5" r="5" fill="none" stroke="#fff" stroke-width="2"/><line x1="10" y1="10" x2="15" y2="15" stroke="#fff" stroke-width="2.4"/></svg>
    <span><svg width="16" height="14" viewBox="0 0 16 14"><path d="M0 1h3l2 8h9l2-6H4" fill="none" stroke="#fff" stroke-width="1.8"/><circle cx="6" cy="12" r="1.5" fill="#fff"/><circle cx="13" cy="12" r="1.5" fill="#fff"/></svg> (0) time</span>
  </div>
</header>

<section class="hero" role="img" aria-label="Sky of soft clouds with a server rack standing on a reflective floor">
  <div class="hero-server"></div>
  <h1 class="hero-title"><span class="l1">Boundless Host offers</span><span class="l2">Effortless Cloud Computing</span></h1>
  <svg class="hero-arrow" style="left:45px" viewBox="0 0 40 40"><circle cx="20" cy="20" r="18" fill="rgba(255,255,255,.4)" stroke="#777" stroke-width="2"/><path d="M23 12l-8 8 8 8" fill="none" stroke="#777" stroke-width="3"/></svg>
  <svg class="hero-arrow" style="left:1111px" viewBox="0 0 40 40"><circle cx="20" cy="20" r="18" fill="rgba(255,255,255,.4)" stroke="#777" stroke-width="2"/><path d="M17 12l8 8-8 8" fill="none" stroke="#777" stroke-width="3"/></svg>
</section>

<section class="welcome">
  <h1>Welcome to Boundless Host</h1>
  <h2>Boundless Host offers Effortless Cloud Computing</h2>
  <p>Boundless Host offers the widest array of products and services based on revolutionary hosted virtual dedicated server and cloud computing technologies. No one rejects, dislikes, or avoids pleasure itself, because it is pleasure, but because those who do not know how to pursue pleasure rationally encounter consequences that are in extremely painful. Nor again is there anyone who loves or pursues or desires to obtain pain of itself, because it is pain, but the because occasionally circumstances occur in which toil and pain can procure him some great pleasure. To take a trivial example, which of us ever in undertakes laborious physical exercise, except to obtain some advantage from it? But who has any right to find fault with a man who chooses to enjoy a pleasure that has no annoying consequences, or one who avoids a pain that produces.</p>
  <div class="btn-dark">READ MORE</div>
</section>

<section class="pricing">
  <h2>Grid for Pricing</h2>
  <p class="intro">There are many variations of passages of Lorem Ipsum available, but the majority have suffered alteration in some form, by injected humour, or randomised words which don't look even slightly believable. If you are going to use a passage of Lorem Ipsum, you need to be sure there isn't anything embarrassing hidden in the middle of text. All the Lorem Ipsum generators on the Internet tend to repeat predefined chunks as necessary, making this the first.</p>

  <div class="plan" style="left:99px">
    <div class="plan-name">Silver</div>
    <div class="plan-price blue"><div class="price-ring"><b>$24.99</b><span>/mon</span></div></div>
    <ul class="plan-features"><li>Included Users 1</li><li>Maximum Users 2</li><li>Included Storage 5 GB</li><li>Maximum Storage 100 GB</li><li>Additional User $24.99</li></ul>
    <div class="plan-cta blue">Build Plan</div>
  </div>
  <div class="plan" style="left:355px">
    <div class="plan-name">Silver</div>
    <div class="plan-price teal"><div class="price-ring"><b>$24.99</b><span>/mon</span></div></div>
    <ul class="plan-features"><li>Included Users 1</li><li>Maximum Users 2</li><li>Included Storage 5 GB</li><li>Maximum Storage 100 GB</li><li>Additional User $24.99</li></ul>
    <div class="plan-cta teal">Build Plan</div>
  </div>
  <div class="plan" style="left:614px">
    <div class="plan-name">Silver</div>
    <div class="plan-price plum"><div class="price-ring"><b>$24.99</b><span>/mon</span></div></div>
    <ul class="plan-features"><li>Included Users 1</li><li>Maximum Users 2</li><li>Included Storage 5 GB</li><li>Maximum Storage 100 GB</li><li>Additional User $24.99</li></ul>
    <div class="plan-cta plum">Build Plan</div>
  </div>
  <div class="plan" style="left:872px">
    <div class="plan-name">Silver</div>
    <div class="plan-price amber"><div class="price-ring"><b>$24.99</b><span>/mon</span></div></div>
    <ul class="plan-features"><li>Included Users 1</li><li>Maximum Users 2</li><li>Included Storage 5 GB</li><li>Maximum Storage 100 GB</li><li>Additional User $24.99</li></ul>
    <div class="plan-cta amber">Build Plan</div>
  </div>
</section>

<main>
  <h2 class="section-title" style="top:1576px">Stream Applications to your Desktop</h2>
  <div class="media" style="top:1628px;height:275px;background:linear-gradient(120deg,#3a3a3a 0%,#8a7e6e 35%,#c9b79a 60%,#6b5c48 100%)" role="img" aria-label="Smartphone with earphones beside a cup of coffee on a wooden table"></div>
  <p class="body-text" style="top:1921px">LoopApp is our application virtualization platform. Stream applications from the cloud; save data in the cloud or on your local computer. Access your applications and data from Panes, Tuxen, Orchard, Slate or Droidix devices. Your users will get the finest desktop experience.</p>
  <span class="read-more" style="top:1995px">READ MORE</span>

  <h2 class="section-title" style="top:2038px">Touch the Cloud<sup style="font-size:12px">TM</sup></h2>
  <div class="media" style="top:2089px;height:277px;background:linear-gradient(180deg,#1f4f8f 0%,#4d86c4 45%,#a9c8e6 75%,#e8eef5 100%)" role="img" aria-label="Hand touching floating glass tiles in a cloudy blue sky"></div>
  <p class="body-text" style="top:2387px">With Boundless Host's Terminal Server plans, you can literally touch the cloud. Connect to your terminal server with a touch-enabled Panes 8 computer, and you can interact with your applications the same way you would if they were installed on your own computer, with your finger. We support any version of Panes, Orchard, Slate, Droidix and Chromix; every plan supports connecting with either a remote desktop client or Internet Browser. Stream the entire desktop or just the applications - it's your choice.</p>
  <span class="read-more" style="top:2480px">READ MORE</span>
  <div class="btn-outline">VIEW MORE BOUNDLESS</div>

  <aside class="features">
    <h3>Features</h3>
    <ul>
      <li><svg width="10" height="10" viewBox="0 0 10 10"><circle cx="5" cy="5" r="4" fill="none" stroke="#c0392b" stroke-width="1.6"/><line x1="2.5" y1="7.5" x2="7.5" y2="2.5" stroke="#c0392b" stroke-width="1.6"/></svg>Access LedgerPro from Anywhere</li>
      <li><svg width="10" height="10" viewBox="0 0 10 10"><circle cx="5" cy="5" r="4" fill="none" stroke="#c0392b" stroke-width="1.6"/><line x1="2.5" y1="7.5" x2="7.5" y2="2.5" stroke="#c0392b" stroke-width="1.6"/></svg>TapCloudTM Enabled</li>
      <li><svg width="10" height="10" viewBox="0 0 10 10"><circle cx="5" cy="5" r="4" fill="none" stroke="#c0392b" stroke-width="1.6"/><line x1="2.5" y1="7.5" x2="7.5" y2="2.5" stroke="#c0392b" stroke-width="1.6"/></svg>Universal Print Drivers</li>
      <li><svg width="10" height="10" viewBox="0 0 10 10"><circle cx="5" cy="5" r="4" fill="none" stroke="#c0392b" stroke-width="1.6"/><line x1="2.5" y1="7.5" x2="7.5" y2="2.5" stroke="#c0392b" stroke-width="1.6"/></svg>Create PDFs</li>
      <li><svg width="10" height="10" viewBox="0 0 10 10"><circle cx="5" cy="5" r="4" fill="none" stroke="#c0392b" stroke-width="1.6"/><line x1="2.5" y1="7.5" x2="7.5" y2="2.5" stroke="#c0392b" stroke-width="1.6"/></svg>Support for Webra, Foxtail, Chromix &amp; Safaro</li>
      <li><svg width="10" height="10" viewBox="0 0 10 10"><circle cx="5" cy="5" r="4" fill="none" stroke="#c0392b" stroke-width="1.6"/><line x1="2.5" y1="7.5" x2="7.5" y2="2.5" stroke="#c0392b" stroke-width="1.6"/></svg>Desktop Support (Panes &amp; Orchard)</li>
      <li><svg width="10" height="10" viewBox="0 0 10 10"><circle cx="5" cy="5" r="4" fill="none" stroke="#c0392b" stroke-width="1.6"/><line x1="2.5" y1="7.5" x2="7.5" y2="2.5" stroke="#c0392b" stroke-width="1.6"/></svg>Mobile Support (Droidix, Slate &amp; Handset)</li>
      <li><svg width="10" height="10" viewBox="0 0 10 10"><circle cx="5" cy="5" r="4" fill="none" stroke="#c0392b" stroke-width="1.6"/><line x1="2.5" y1="7.5" x2="7.5" y2="2.5" stroke="#c0392b" stroke-width="1.6"/></svg>Daily Onsite &amp; Offsite Backup</li>
      <li><svg width="10" height="10" viewBox="0 0 10 10"><circle cx="5" cy="5" r="4" fill="none" stroke="#c0392b" stroke-width="1.6"/><line x1="2.5" y1="7.5" x2="7.5" y2="2.5" stroke="#c0392b" stroke-width="1.6"/></svg>Restore Files with Explorer</li>
      <li><svg width="10" height="10" viewBox="0 0 10 10"><circle cx="5" cy="5" r="4" fill="none" stroke="#c0392b" stroke-width="1.6"/><line x1="2.5" y1="7.5" x2="7.5" y2="2.5" stroke="#c0392b" stroke-width="1.6"/></svg>OfficeDesk Suite</li>
      <li><svg width="10" height="10" viewBox="0 0 10 10"><circle cx="5" cy="5" r="4" fill="none" stroke="#c0392b" stroke-width="1.6"/><line x1="2.5" y1="7.5" x2="7.5" y2="2.5" stroke="#c0392b" stroke-width="1.6"/></svg>Multifactor Authentication</li>
      <li><svg width="10" height="10" viewBox="0 0 10 10"><circle cx="5" cy="5" r="4" fill="none" stroke="#c0392b" stroke-width="1.6"/><line x1="2.5" y1="7.5" x2="7.5" y2="2.5" stroke="#c0392b" stroke-width="1.6"/></svg>Intrusion Detection &amp; Prevention</li>
      <li><svg width="10" height="10" viewBox="0 0 10 10"><circle cx="5" cy="5" r="4" fill="none" stroke="#c0392b" stroke-width="1.6"/><line x1="2.5" y1="7.5" x2="7.5" y2="2.5" stroke="#c0392b" stroke-width="1.6"/></svg>Encrypted Communications</li>
      <li><svg width="10" height="10" viewBox="0 0 10 10"><circle cx="5" cy="5" r="4" fill="none" stroke="#c0392b" stroke-width="1.6"/><line x1="2.5" y1="7.5" x2="7.5" y2="2.5" stroke="#c0392b" stroke-width="1.6"/></svg>SSAE 16 Type 2 / SOC 1</li>
      <li><svg width="10" height="10" viewBox="0 0 10 10"><circle cx="5" cy="5" r="4" fill="none" stroke="#c0392b" stroke-width="1.6"/><line x1="2.5" y1="7.5" x2="7.5" y2="2.5" stroke="#c0392b" stroke-width="1.6"/></svg>24/7/365 U.S. Based Support</li>
      <li><svg width="10" height="10" viewBox="0 0 10 10"><circle cx="5" cy="5" r="4" fill="none" stroke="#c0392b" stroke-width="1.6"/><line x1="2.5" y1="7.5" x2="7.5" y2="2.5" stroke="#c0392b" stroke-width="1.6"/></svg>30-day 100% Money Back Guarantee</li>
    </ul>
  </aside>

  <div class="guarantee-seal" role="img" aria-label="Gold 30-day money back guarantee seal"></div>

  <div class="partners">
    <div class="partner" style="width:72px;height:72px;border-radius:50%"></div>
    <div class="partner" style="width:90px;height:40px"></div>
    <div class="partner" style="width:56px;height:86px"></div>
  </div>
</main>

<footer class="site-footer">
  <ul class="foot-col" style="left:99px"><li>Our Success Stories</li><li>Our Technology</li><li>Our Guarantee</li></ul>
  <div class="foot-rule" style="left:265px"></div>
  <ul class="foot-col" style="left:285px"><li>Terms &amp; Conditions</li><li>Privacy Policy</li><li>Acceptable Use Policy</li></ul>
  <div class="foot-rule" style="left:442px"></div>
  <ul class="foot-col" style="left:487px"><li>Articles</li><li>Videos</li><li>Newsroom</li><li>System Status</li></ul>
  <div class="foot-rule" style="left:603px"></div>
  <ul class="foot-col" style="left:632px"><li>Support</li><li>Virtual Server Web Access</li><li>LoopProtect CMC</li><li>LoopApp Login</li></ul>
  <div class="foot-rule" style="left:810px"></div>
  <ul class="foot-col" style="left:848px"><li>Contact Us</li><li>Become a Partner</li><li>Find us on Circles+</li></ul>
  <div class="foot-rule" style="left:1000px"></div>
  <ul class="foot-col social" style="left:1025px"><li><i></i>facenet</li><li><i></i>linkpro</li><li><i></i>chirper</li><li><i></i>searchly</li></ul>
  <div class="copyright">© 2010 Boundless Host</div>
  <div class="page-code">C 19</div>
</footer>

</body>
</html>
```